Yard Sign Design Needed

Yard sign needed for mowing & landscaping company. Would like to use the top logo with black background which is attached. Would like MOWING to be in large standout letters. The word "landscaping" can be smaller and more artistic or omitted. Will need room for phone number once design is approved. The phone number will need to stand out and look identical/similar to the word 'MOWING"

```html
<!DOCTYPE html>
<html lang="en">
<head>
<meta charset="utf-8">
<title>Dalvern Contractors – Yard Signs</title>
<link rel="stylesheet" href="https://fonts.googleapis.com/css2?family=Anton&family=Audiowide&family=Oswald:wght@700&display=swap">
<style>
  :root {
    --stage: #a3a3a3;
    --ink: #000000;
    --paper: #ffffff;
    --lime: #8ea70a;
    --font-round: "Audiowide", sans-serif;
    --font-condensed: "Anton", sans-serif;
    --font-tag: "Oswald", sans-serif;
  }
  * { box-sizing: border-box; margin: 0; padding: 0; }
  html, body { width: 1200px; height: 780px; overflow: hidden; }
  body { background: var(--stage); position: relative; }

  .sign {
    position: absolute;
    overflow: hidden;
    box-shadow: 2px 3px 6px rgba(0,0,0,0.45);
    background: var(--ink);
  }
  .sign--classic { left: 119px; top: 82px; width: 463px; height: 614px; }
  .sign--angled  { left: 624px; top: 80px;  width: 460px; height: 615px; }

  .sign__bg { position: absolute; inset: 0; width: 100%; height: 100%; }

  /* brand block */
  .brand-mark { position: absolute; background: var(--lime); }
  .brand-name {
    position: absolute;
    font-family: var(--font-round);
    color: var(--lime);
    text-align: center;
    line-height: 1;
  }
  .brand-name__main { display: block; }
  .brand-name__sub { display: block; }

  .sign--classic .brand-mark { left: 186px; top: 70px; width: 90px; height: 90px; }
  .sign--classic .brand-name { left: 0; right: 0; top: 228px; }
  .sign--classic .brand-name__main { font-size: 44px; letter-spacing: 1px; }
  .sign--classic .brand-name__sub { font-size: 21px; margin-top: 8px; letter-spacing: 1px; }

  .sign--angled .brand-mark { left: 74px; top: 70px; width: 64px; height: 64px; }
  .sign--angled .brand-name { left: 160px; top: 74px; text-align: left; }
  .sign--angled .brand-name__main { font-size: 31px; }
  .sign--angled .brand-name__sub { font-size: 16px; margin-top: 6px; }

  /* classic sign */
  .service-band {
    position: absolute; left: 0; right: 0; top: 368px; height: 113px;
    background: var(--paper); text-align: center;
  }
  .service-band__title {
    font-family: var(--font-round);
    font-size: 78px; line-height: 1; color: var(--ink);
    margin-top: 4px; letter-spacing: 1px;
  }
  .service-band__tag {
    font-family: var(--font-round);
    font-size: 20px; color: var(--lime);
    letter-spacing: 2px; margin-top: 2px;
  }
  .phone-tab {
    position: absolute; left: 43px; width: 376px; top: 538px; height: 76px;
    background: var(--lime); border-radius: 10px 10px 0 0;
    text-align: center;
  }
  .phone {
    font-family: var(--font-condensed);
    color: var(--paper); line-height: 1;
  }
  .phone-tab .phone { font-size: 58px; margin-top: 6px; }

  /* angled sign */
  .headline {
    position: absolute; left: 32px; width: 392px; top: 268px;
    font-family: var(--font-condensed);
    font-size: 118px; line-height: 1; color: var(--ink);
    text-align: center; letter-spacing: 1px;
  }
  .headline-tag {
    position: absolute; right: 36px; top: 372px;
    font-family: var(--font-tag);
    font-size: 36px; line-height: 1; color: var(--lime);
    letter-spacing: 1px;
  }
  .sign--angled .phone {
    position: absolute; left: 0; right: 0; top: 530px;
    text-align: center; font-size: 62px;
  }
</style>
</head>
<body>

<section class="sign sign--classic" aria-label="Yard sign, stacked layout">
  <div class="brand-mark"></div>
  <div class="brand-name">
    <span class="brand-name__main">DALVERN</span>
    <span class="brand-name__sub">CONTRACTORS LLC</span>
  </div>
  <div class="service-band">
    <p class="service-band__title">mowing</p>
    <p class="service-band__tag">LANDSCAPING</p>
  </div>
  <div class="phone-tab">
    <p class="phone">333-333-3333</p>
  </div>
</section>

<section class="sign sign--angled" aria-label="Yard sign, angled layout">
  <svg class="sign__bg" viewBox="0 0 575 769" preserveAspectRatio="none" aria-hidden="true">
    <rect width="575" height="769" fill="var(--ink)"/>
    <polygon points="0,268 418,226 0,300" fill="var(--paper)"/>
    <polygon points="0,318 575,205 575,769 0,769" fill="var(--paper)"/>
    <polygon points="575,540 575,556 160,637" fill="var(--lime)"/>
    <polygon points="0,660 575,592 575,769 0,769" fill="var(--lime)"/>
  </svg>
  <div class="brand-mark"></div>
  <div class="brand-name">
    <span class="brand-name__main">DALVERN</span>
    <span class="brand-name__sub">CONTRACTORS LLC</span>
  </div>
  <p class="headline">MOWING</p>
  <p class="headline-tag">landscaping</p>
  <p class="phone">333-333-3333</p>
</section>

</body>
</html>
```